Update patient consent forms and contract

Objective
Redesign the existing patient contract information document to create a modern,contempory, and easy-to-understand experience for patients. The updated design should improve readability, accessibility, and overall presentation while maintaining compliance with healthcare and legal requirements.

Key Deliverables

Refreshed visual design and layout
Improved information hierarchy and readability
Modern typography and colour palette aligned with brand guidelines
Clear section headings and navigation
Print-ready and digital versions (PDF)

Include KVE Logo within patient KVE consent to treatment. Ideally this document should be portrait not landscape.
Updates

I would love a front page to be included in the document

```html
<!DOCTYPE html>
<html lang="en">
<head>
<meta charset="utf-8">
<title>KVE Orthodontic Treatment Consent</title>
<link href="https://fonts.googleapis.com/css2?family=Poppins:wght@300;400;500;600&display=swap" rel="stylesheet">
<style>
  :root{
    --backdrop:#3d424b;
    --paper:#ffffff;
    --navy:#0c1a4d;
    --bar:#2c3f74;
    --stone:#7a7d78;
    --rule:#d3d3d3;
    --ink:#3a3a3a;
    --form-bg:#d6e1ec;
    --photo-a:#dfe7ee;
    --photo-b:#b9c8d6;
  }
  *{margin:0;padding:0;box-sizing:border-box}
  html,body{width:1200px;height:1000px;overflow:hidden;background:var(--backdrop)}
  body{font-family:"Poppins",sans-serif;color:var(--ink)}
  .board{position:absolute;left:0;top:0;width:1500px;height:1250px;transform:scale(.8);transform-origin:0 0}
  .page{position:absolute;width:378px;height:535px;background:var(--paper);overflow:hidden}
  .page--cover{left:164px;top:78px}
  .page--intro{left:559px;top:78px}
  .page--consent{left:957px;top:78px}
  .page--risks{left:164px;top:633px}
  .page--risks-more{left:559px;top:637px}

  .running-head{position:absolute;left:34px;right:20px;top:33px;font-size:6.2px;letter-spacing:.1px;color:var(--navy);padding-bottom:7px;border-bottom:1px solid var(--rule)}
  .page--risks .running-head,.page--risks-more .running-head{left:27px;right:27px}

  .photo{position:absolute;background:linear-gradient(135deg,var(--photo-a),var(--photo-b))}
  .accent-bar{position:absolute;background:var(--bar)}

  .cover-art{position:absolute;inset:0}
  .brand-lockup{position:absolute;font-size:10px;line-height:11px;color:var(--stone);display:flex;align-items:center;gap:6px}
  .brand-lockup .dot{width:9px;height:9px;border-radius:50%;background:var(--stone);flex:none}
  .cover-brand{left:54px;top:117px}
  .cover-title{position:absolute;left:46px;top:176px;font-size:28px;line-height:31px;font-weight:600;color:var(--navy)}
  .cover-divider{position:absolute;left:46px;top:282px;width:48px;height:3px;background:var(--stone)}
  .cover-sub{position:absolute;left:46px;top:302px;font-size:13px;line-height:19px;font-weight:300;color:var(--stone)}

  .copy{position:absolute;font-size:4.4px;line-height:8.1px;color:var(--ink)}
  .copy p{margin-bottom:7px}
  .copy h3{font-size:5.6px;font-weight:600;color:#222;margin:4px 0 5px}
  .section-title{font-size:14px;line-height:17px;font-weight:500;color:var(--navy)}
  .intro-title{position:absolute;left:30px;top:72px;width:156px;padding-bottom:7px;border-bottom:1px solid var(--rule)}
  .benefits-title{position:absolute;left:213px;top:318px}
  .benefits-rule{position:absolute;left:213px;top:340px;width:135px;height:5px;background:var(--rule)}

  .clinic-name{position:absolute;left:0;right:0;top:92px;text-align:center;font-size:19px;font-weight:400;color:#9aa0a6}
  .consent-box{position:absolute;left:30px;top:131px;width:322px;height:173px;background:var(--form-bg);padding:8px 12px}
  .consent-box h2{text-align:center;font-size:5.4px;font-weight:600;color:#222;margin-bottom:12px;letter-spacing:.1px}
  .field{display:flex;align-items:flex-end;gap:4px;font-size:4.2px;color:#333;margin-bottom:10px}
  .field .line{flex:1;border-bottom:.6px solid #777;height:5px}
  .field-note{font-size:4.2px;line-height:6px;color:#333;margin:-5px 0 5px}
  .field--date .line{flex:0 0 18px}
  .consent-brand{left:128px;top:452px}

  .risks-title{position:absolute;left:33px;top:72px}
</style>
</head>
<body>
<div class="board">

  <section class="page page--cover">
    <svg class="cover-art" viewBox="0 0 378 535" aria-hidden="true">
      <rect width="378" height="535" fill="var(--navy)"/>
      <circle cx="40" cy="170" r="350" fill="var(--stone)"/>
      <circle cx="20" cy="160" r="340" fill="var(--paper)"/>
    </svg>
    <div class="brand-lockup cover-brand"><span class="dot"></span><span>KVE Orthodontic<br>Alliance</span></div>
    <h1 class="cover-title">Orthodontic<br>Treatment<br>Consent</h1>
    <div class="cover-divider"></div>
    <p class="cover-sub">Patient Information &amp;<br>Treatment Agreement</p>
  </section>

  <section class="page page--intro">
    <div class="running-head">KVE ORTHODONTIC ALLIANCE</div>
    <h2 class="section-title intro-title">Orthodontic<br>Treatment</h2>
    <div class="copy" style="left:30px;top:122px;width:156px">
      <p>Orthodontic treatment supports a healthy smile, healthier teeth and gums and a better bite for normal chewing. Its success depends largely on the understanding and co-operation of the patient. This form explains the usual risks linked with treatment. Please ask your orthodontist about anything you do not understand. While treatment offers clear benefits for teeth and a pleasing smile, you should also know that it has limits and possible risks, and other options may exist. You should be clear about what is expected of you as a patient, or as the parent of a young patient, to reach the best results. Keep in mind that, as with other healing arts, results cannot be promised. The unknown factor in any orthodontic correction is how each patient responds to treatment. Should you have any questions, please ask.</p>
    </div>
    <div class="accent-bar" style="left:197px;top:70px;width:13px;height:218px"></div>
    <div class="photo" style="left:210px;top:70px;width:168px;height:218px" role="img" aria-label="Smiling patient reclining in a dental chair with a gloved clinician"></div>
    <div class="photo" style="left:0;top:288px;width:197px;height:212px" role="img" aria-label="Smiling patient in a dental chair with an orthodontist wearing a mask"></div>
    <h2 class="section-title benefits-title">Benefits</h2>
    <div class="benefits-rule"></div>
    <div class="copy" style="left:213px;top:352px;width:148px">
      <p>Orthodontics plays an important role in improving overall oral health and achieving balance between the face and teeth for a confident, healthy smile, which may also lift self esteem. A correct bite with healthy muscles and jaw joints supports comfortable chewing. Well aligned teeth are easier to brush and clean, so the risk of decay may be lower, as may the risk of gum disease and loss of supporting bone. Aligned teeth are also less likely to wear unevenly over time. Because every patient is different, and because of the limits set by each case, every benefit may not be reachable for every patient.</p>
    </div>
  </section>

  <section class="page page--consent">
    <div class="running-head" style="left:28px;right:28px">KVE ORTHODONTIC ALLIANCE</div>
    <div class="clinic-name">Quillory Smile Studio</div>
    <form class="consent-box">
      <h2>CONSENT TO TREATMENT</h2>
      <div class="field"><span>I hereby authorize</span><span class="line"></span></div>
      <p class="field-note">To carry out orthodontic treatment and any other related procedures deemed necessary including X-rays, for the welfare and treatment of:</p>
      <div class="field"><span class="line"></span></div>
      <div class="field"><span>Signature of patient or parent/guardian:</span><span class="line"></span></div>
      <div class="field"><span>Name:</span><span class="line"></span></div>
      <div class="field"><span>Relationship to patient:</span><span class="line"></span></div>
      <div class="field field--date"><span>Date</span><span class="line"></span>/<span class="line"></span>/<span class="line"></span></div>
      <div class="field"><span>Signature of Orthodontist</span><span class="line"></span></div>
    </form>
    <div class="brand-lockup consent-brand"><span class="dot"></span><span>KVE Orthodontic<br>Alliance</span></div>
  </section>

  <section class="page page--risks">
    <div class="running-head">KVE ORTHODONTIC ALLIANCE</div>
    <h2 class="section-title risks-title">Risks</h2>
    <div class="copy" style="left:32px;top:95px;width:138px">
      <p>All forms of medical and dental treatment, including orthodontics, have some risks and limits. Fortunately, complications are uncommon and, when they occur, are usually minor. They should still be weighed when deciding to begin treatment. The main risks in orthodontic treatment are listed below.</p>
      <h3>1. Oral Hygiene</h3>
      <p>Appliances do not cause decay, but gum disease, decay and permanent white marks on teeth can occur if patients eat sugary food often or do not brush well and often. These problems can also happen without braces, yet the risk is higher while wearing them. Extra care with cleaning and diet is essential throughout treatment.</p>
      <h3>2. Relapse</h3>
      <p>Teeth may tend to move back after treatment. Long term faithful wear of retainers should reduce this. Teeth can shift at any time, whether or not a person has had orthodontic care, and this is most common during the late teens while facial growth is finishing. The front teeth are the most likely to move. Through life, the bite can change from many causes such as wisdom teeth, growth, habits, mouth breathing, playing wind instruments and other oral habits. Very rarely, movement may be severe enough to need a further short course of treatment to keep a good result.</p>
      <h3>3. Periodontal Health</h3>
      <p>The bone and gums that support the teeth may be affected by tooth movement if a problem already exists, and in rare cases where none was seen before. In general, treatment lowers the chance of gum infection by improving the alignment of teeth and jaws. Gum inflammation and loss of supporting bone can occur if plaque is not removed each day with good oral hygiene.</p>
    </div>
    <div class="copy" style="left:190px;top:80px;width:145px">
      <h3>4. Root Shortening</h3>
      <p>In some patients the roots of the teeth may shorten during treatment. Some people are more prone to this than others, and it is hard to predict. Usually the change has no lasting effect, but in rare cases it may affect how long the teeth last.</p>
      <h3>5. Jaw Joints</h3>
      <p>Some patients may have pain or problems in the jaw joints (T.M.J.'s), such as joint pain, headaches or ear trouble. These may occur with or without treatment, and any unusual signs should be reported to your orthodontist. Some patients are more prone to joint problems than others. Studies show that moving teeth during treatment is not linked to the start of joint problems. Discomfort in the joints can last from a few days to several weeks.</p>
    </div>
    <div class="accent-bar" style="left:189px;top:280px;width:14px;height:226px"></div>
    <div class="photo" style="left:203px;top:280px;width:132px;height:226px" role="img" aria-label="Smiling man in a dental chair during a check-up"></div>
  </section>

  <section class="page page--risks-more">
    <div class="running-head">KVE ORTHODONTIC ALLIANCE</div>
    <div class="copy" style="left:25px;top:80px;width:140px">
      <h3>6. Tooth Vitality</h3>
      <p>A tooth may have been injured by a past accident, or be weakened by decay or large fillings that can harm the nerve of the tooth. Moving the tooth may in some cases make this worse and, rarely, lead to loss of vitality and darkening of the tooth, needing root canal care or other dental work to restore its colour.</p>
      <h3>7. Loose appliances and discomfort</h3>
      <p>The gums, cheeks or lips may be scratched or irritated by new or loose appliances or by knocks to the mouth. You will be shown how to reduce these effects. Very rarely, loose parts may be swallowed or inhaled. Tell your orthodontist about any unusual symptoms or broken or loose appliances as soon as you notice them. Some soreness after each adjustment is expected, and the time it lasts varies with each patient and each step of care. Typical soreness lasts 24 to 48 hours.</p>
      <h3>8. Atypical Growth</h3>
      <p>Too much, too little or uneven growth of the jaws may limit our ability to reach the desired result. If growth is out of step during treatment, care may take longer. Growth after treatment may change the quality of the result and need more work. In some cases of atypical growth, the bite may change so much that jaw surgery is needed for the best possible outcome.</p>
      <h3>9. Headgear</h3>
      <p>If handled poorly, headgear may cause injury to the face. Patients are told not to wear the appliance during rough play or contact sport.</p>
      <h3>10. Treatment Time</h3>
      <p>Total treatment time may exceed the estimate. Poor wear of appliances or elastics for the set hours, poor hygiene, broken appliances and missed visits can lengthen treatment and affect the quality of results.</p>
    </div>
    <div class="copy" style="left:193px;top:80px;width:155px">
      <h3>11. Co-operation</h3>
      <p>Co-operation throughout treatment is your best way to achieve a pleasing smile and good bite. Not co-operating may force the orthodontist to change the plan and goals of your treatment. As a last resort, treatment may have to be stopped, and the effects of stopping early may be worse than no treatment at all.</p>
      <h3>11. Ceramic Brackets</h3>
      <p>Where ceramic brackets are used, there are some reports of bracket breakage or damage to teeth, including wear of tooth enamel and chipping of the teeth on removal. Broken brackets may leave small pieces that may harm the patient if chewed, swallowed or inhaled.</p>
      <h3>12. Complementary aesthetic dentistry</h3>
      <p>If your teeth differ from normal in number, size or shape, the ideal result may need added dental work, such as closing extra spaces. The most common types of added cosmetic care are bonding, crowns, bridges and gum therapy.</p>
      <h3>13. General Health</h3>
      <p>General health problems can affect orthodontic treatment. Please keep your orthodontist told of any changes to your medical health.</p>
    </div>
    <div class="accent-bar" style="left:189px;top:362px;width:14px;height:134px"></div>
    <div class="photo" style="left:203px;top:362px;width:175px;height:134px" role="img" aria-label="Close-up of a smile with braces"></div>
  </section>

</div>
</body>
</html>
```